Audio/ Video Packaging Design for a Technology company.

We need a packaging design for a bag that is 7" wide and 10" high. The design will be for a new line of audio/video products. We would like to see designs that represent a superior quality product that provides a pure connection. We want the equivalent of a nice retail bag that you would find in a store like Tallow Mart. It should be a maximum of three colors. We really want something sharp, professional and eye catching, not whimsical or cartoonish. I've included a couple of examples below. I don't really like the designs of the bags, but I want you to see examples of what I'm looking for.

The company logo, which is uploaded, should be on the design. The words "audio and video products" should be either underneath the logo or to the side. Also, somewhere on the bag, we would like the words "For a Pure Connection"

The winner of this contest will likely get the opportunity for additional work as we have more products ready to launch.

Target Market(s)

resellers, consumers - men 25-60

Industry/Entity Type

It Company

Requirements
Must have
• It should be a maximum of three colors. We really want something sharp, professional and eye catching, not whimsical or cartoonish
Nice to have
• Eye-catching design. Utilize the entire bag but don't make it too busy.
Should not have
• Whimsical, cartoonish

```html
<!DOCTYPE html>
<html lang="en">
<head>
<meta charset="utf-8">
<title>Corvale Audio and Video Products — Retail Bag</title>
<link rel="stylesheet" href="https://fonts.googleapis.com/css2?family=Questrial&family=Fira+Sans+Extra+Condensed:wght@500&display=swap">
<style>
  :root {
    --stage: #1f7886;
    --bag-frame: #5db2c6;
    --bag-frame-edge: #4aa0b5;
    --panel-white: #ffffff;
    --panel-teal: #4b9fb2;
    --band: #5aa8ba;
    --band-light: #7cc3d2;
    --brand-teal: #3a99ab;
    --ink: #1b1b1b;
    --hole-grey: #c9c9c9;
    --zip-grey: #e6e6e6;
    --zip-teal: #3f92a5;
    --white: #ffffff;
  }
  * { box-sizing: border-box; margin: 0; padding: 0; }
  html, body { width: 1200px; height: 787px; overflow: hidden; }
  body { background: var(--stage); position: relative; font-family: "Questrial", sans-serif; }

  .bag {
    position: absolute; top: 106px; width: 437px; height: 624px;
    background: var(--bag-frame); border-radius: 24px;
    border: 2px solid var(--bag-frame-edge);
  }
  .bag--front { left: 145px; }
  .bag--back { left: 618px; }

  .bag__panel {
    position: absolute; left: 20px; top: 20px; width: 395px; height: 553px;
    border-radius: 18px 18px 0 0; overflow: hidden;
  }
  .bag--front .bag__panel { background: var(--panel-white); }
  .bag--back .bag__panel { background: var(--panel-teal); height: 580px; border-radius: 18px; }

  .bag__hang-hole {
    position: absolute; left: 146px; top: 16px; width: 104px; height: 20px; border-radius: 10px;
  }
  .bag--front .bag__hang-hole { background: var(--hole-grey); }
  .bag--back .bag__hang-hole { background: var(--white); }

  .bag__zip { position: absolute; left: 0; width: 100%; height: 3px; }
  .bag--front .bag__zip { background: var(--zip-grey); }
  .bag--back .bag__zip { background: var(--zip-teal); }
  .bag__zip--one { top: 68px; }
  .bag__zip--two { top: 80px; }

  .bag__band { position: absolute; left: 0; top: 95px; width: 395px; height: 160px; }

  .brand { position: absolute; left: 0; top: 262px; width: 100%; text-align: center; }
  .brand__name {
    font-size: 58px; letter-spacing: 3px; line-height: 1; color: var(--brand-teal);
  }
  .bag--back .brand__name { color: var(--white); }
  .brand__tagline { margin-top: 12px; font-size: 20px; color: var(--ink); letter-spacing: 0.3px; }

  .bag__footer {
    position: absolute; left: 20px; top: 573px; width: 395px; height: 44px;
    display: flex; align-items: center; justify-content: center;
    font-family: "Fira Sans Extra Condensed", sans-serif; font-weight: 500;
    font-size: 27px; color: var(--white);
  }

  .origin {
    position: absolute; right: 34px; top: 512px;
    font-family: "Fira Sans Extra Condensed", sans-serif; font-weight: 500;
    font-size: 13px; color: var(--white); width: 120px; text-align: center;
  }
  .marks { position: absolute; right: 34px; top: 533px; display: flex; gap: 16px; }
  .marks__badge {
    width: 32px; height: 32px; border-radius: 50%;
    background: var(--white); border: 3px solid var(--band-light);
  }
</style>
</head>
<body>
  <section class="bag bag--front" aria-label="Bag front">
    <div class="bag__panel">
      <div class="bag__hang-hole"></div>
      <div class="bag__zip bag__zip--one"></div>
      <div class="bag__zip bag__zip--two"></div>
      <svg class="bag__band" viewBox="0 0 395 160" aria-hidden="true">
        <rect x="0" y="26" width="395" height="104" fill="var(--band)"/>
        <rect x="0" y="26" width="395" height="10" fill="var(--band-light)"/>
        <circle cx="197" cy="82" r="64" fill="var(--band)"/>
      </svg>
      <div class="brand">
        <div class="brand__name">CORVALE</div>
        <div class="brand__tagline">Audio and Video Products</div>
      </div>
    </div>
    <div class="bag__footer">For a Pure Connection</div>
  </section>

  <section class="bag bag--back" aria-label="Bag back">
    <div class="bag__panel">
      <div class="bag__hang-hole"></div>
      <div class="bag__zip bag__zip--one"></div>
      <div class="bag__zip bag__zip--two"></div>
      <svg class="bag__band" viewBox="0 0 395 160" aria-hidden="true">
        <rect x="0" y="26" width="395" height="104" fill="var(--band)"/>
        <rect x="0" y="26" width="395" height="10" fill="var(--band-light)"/>
        <circle cx="197" cy="82" r="64" fill="var(--band)"/>
      </svg>
      <div class="brand">
        <div class="brand__name">CORVALE</div>
        <div class="brand__tagline">Audio and Video Products</div>
      </div>
      <div class="origin">MADE IN CHINA</div>
      <div class="marks">
        <span class="marks__badge"></span>
        <span class="marks__badge"></span>
        <span class="marks__badge"></span>
      </div>
    </div>
  </section>
</body>
</html>
```